LEAP GLIDE SOAR

Need a 4 X 6 post card design. Here are the elements that need to be on the card:
LEAP, GLIDE, SOAR (This is the title please feel free and create)
DATE: August 28, 2022
Showtimes 2:30 PM & 7:30 PM
Location: Harriet Colvane Theatre Walnut Creek, CA
Tickets can be purchased at:
http://colvanestagehall.tixora-example.com/LEAPGLIDESOAR or
by calling the ticket office at (925) 555-STAGE
LEAP, GLIDE, SOAR showcases the dance stylings of urban hip hop, ballet, modern jazz and much much more! Bay Area renown dancer/choreographer Rosa Janelle Pruitt headlines this cast of dancers and will amaze you as she takes you on a journey through dance that you will never forget. Join us for an experience that will prove to excite and delight you!
Now for the artwork I would like to incorporate all three of these photos. The photo entitled "beach" you are only to use the dancer on the left. So clip out the other dancer in the pink dress. The Garden photo and the beach photo the images need to be cut out from the background. The sidewalk photo you can leave the background (just my preference) but for the sake of the overall design I'm ok with removing its background as well.
Ok have at it. I want to end this competition in a few days so let's get these designs in. Thank you!

```html
<!DOCTYPE html>
<html lang="en">
<head>
<meta charset="utf-8">
<title>Leap, Glide, Soar — Postcard</title>
<link href="https://fonts.googleapis.com/css2?family=Great+Vibes&family=Quicksand:wght@600;700&family=Raleway:wght@200;300&display=swap" rel="stylesheet">
<style>
  :root {
    --stage: #575252;
    --violet: #6a2c96;
    --indigo: #5b4fc2;
    --magenta: #e8348a;
    --coral: #f2584f;
    --blush: #f7a3cf;
    --white: #ffffff;
  }
  html, body {
    margin: 0;
    width: 1200px;
    height: 865px;
    overflow: hidden;
    background: var(--stage);
  }
  .postcard {
    position: absolute;
    left: 0;
    top: 33px;
    width: 1200px;
    height: 800px;
    overflow: hidden;
    color: var(--white);
    background:
      radial-gradient(circle at 6% 8%, #5c5ad0 0%, rgba(92,90,208,0) 30%),
      radial-gradient(circle at 38% 20%, #6f4fc4 0%, rgba(111,79,196,0) 26%),
      radial-gradient(circle at 96% 4%, #f7743f 0%, rgba(247,116,63,0) 35%),
      radial-gradient(circle at 30% 70%, #ee3a8c 0%, rgba(238,58,140,0) 45%),
      linear-gradient(115deg, #9b3fb8 0%, #d8368f 40%, var(--magenta) 60%, var(--coral) 100%);
  }
  .artwork { position: absolute; inset: 0; }

  .title {
    position: absolute;
    inset: 0 0 auto 0;
    height: 150px;
    margin: 0;
    font-family: "Great Vibes", cursive;
    font-weight: 400;
    font-size: 112px;
    line-height: 1;
  }
  .title span { position: absolute; top: 22px; white-space: nowrap; }
  .title .w1 { left: 44px; }
  .title .w2 { left: 408px; }
  .title .w3 { left: 826px; }

  .details { position: absolute; left: 51px; top: 0; }
  .details .line {
    position: absolute;
    left: 0;
    margin: 0;
    white-space: nowrap;
    font-size: 21px;
    line-height: 30px;
    transform: translateY(-50%);
  }
  .label { font-family: "Raleway", sans-serif; font-weight: 200; }
  .value { font-family: "Quicksand", sans-serif; font-weight: 700; }
  .value small { font-size: 0.72em; }
  .details .url { font-size: 19px; }

  .blurb { position: absolute; left: 51px; top: 545px; }
  .blurb-title {
    margin: 0;
    font-family: "Great Vibes", cursive;
    font-weight: 400;
    font-size: 42px;
    line-height: 48px;
  }
  .blurb-text {
    margin: 0;
    font-family: "Quicksand", sans-serif;
    font-weight: 700;
    font-size: 20.5px;
    line-height: 30px;
    letter-spacing: -0.5px;
    white-space: nowrap;
  }
</style>
</head>
<body>
<main class="postcard">
  <svg class="artwork" width="1200" height="800" viewBox="0 0 1200 800">
    <defs>
      <linearGradient id="scarfTone" x1="0" y1="0" x2="1" y2="0">
        <stop offset="0" stop-color="#5a3fb0" stop-opacity="0.8"/>
        <stop offset="1" stop-color="#7a4fc8" stop-opacity="0.8"/>
      </linearGradient>
      <linearGradient id="whiteTone" x1="0" y1="0" x2="0" y2="1">
        <stop offset="0" stop-color="#f4f2f5"/>
        <stop offset="1" stop-color="#dcd8df"/>
      </linearGradient>
      <linearGradient id="blackTone" x1="0" y1="0" x2="0" y2="1">
        <stop offset="0" stop-color="#2e2833"/>
        <stop offset="1" stop-color="#141217"/>
      </linearGradient>
      <linearGradient id="pinkTone" x1="0" y1="0" x2="0" y2="1">
        <stop offset="0" stop-color="#df45a6"/>
        <stop offset="1" stop-color="#c83b98"/>
      </linearGradient>
    </defs>

    <path class="lower-band" fill="var(--violet)"
          d="M0,535 C110,500 240,492 380,492 L663,499 C800,470 900,420 980,330 C1060,240 1130,150 1200,56 L1200,800 L0,800 Z"/>
    <path class="band-edge" fill="none" stroke="var(--blush)" stroke-width="5"
          d="M0,535 C110,500 240,492 380,492 L663,499"/>
    <path class="band-edge" fill="none" stroke="var(--blush)" stroke-width="2.5" stroke-opacity="0.75"
          d="M700,500 C780,480 850,450 930,405"/>

    <rect class="photo photo-scarf" role="img" aria-label="Photo of a dancer in white lifting a violet scarf overhead"
          x="496" y="165" width="460" height="255" rx="90" fill="url(#scarfTone)"/>
    <rect class="photo photo-white-dancer" role="img" aria-label="Photo of the dancer in white, full length"
          x="760" y="260" width="150" height="436" rx="60" fill="url(#whiteTone)"/>
    <rect class="photo photo-black-dancer" role="img" aria-label="Photo of a dancer in a black leotard and skirt in an arabesque"
          x="674" y="300" width="262" height="482" rx="70" fill="url(#blackTone)"/>
    <rect class="photo photo-headliner" role="img" aria-label="Photo of the headlining choreographer in a fuchsia gown"
          x="932" y="124" width="224" height="676" rx="80" fill="url(#pinkTone)"/>
  </svg>

  <h1 class="title" aria-label="Leap, Glide, Soar">
    <span class="w1">Leap,</span>
    <span class="w2">Glide,</span>
    <span class="w3">Soar</span>
  </h1>

  <section class="details">
    <p class="line" style="top:163px"><span class="label">DATE: </span><span class="value">August 28, 2022</span></p>
    <p class="line" style="top:199px"><span class="label">Showtimes </span><span class="value">2:30<small>PM</small> &amp; 7:30<small>PM</small></span></p>
    <p class="line" style="top:234px"><span class="label">Location:</span></p>
    <p class="line" style="top:264px"><span class="value">Harriet Colvane Theatre</span></p>
    <p class="line" style="top:294px"><span class="value">Walnut Creek, CA</span></p>
    <p class="line" style="top:330px"><span class="label">Tickets can be purchased at:</span></p>
    <p class="line url" style="top:366px"><span class="value">http://colvanestagehall.tixora-example.com/</span></p>
    <p class="line url" style="top:396px"><span class="value">LEAPGLIDESOAR</span></p>
    <p class="line" style="top:431px"><span class="label">or by calling the ticket office at</span></p>
    <p class="line" style="top:461px"><span class="value">(925) 555-STAGE</span></p>
  </section>

  <section class="blurb">
    <p class="blurb-title">Leap, Glide, Soar</p>
    <p class="blurb-text">showcases the dance stylings of urban hip hop, ballet,<br>modern jazz and much much more! Bay Area renown<br>dancer/choreographer Rosa Janelle Pruitt headlines this cast<br>of dancers and will amaze you as she takes you on a journey<br>through dance that you will never forget. Join us for an<br>experience that will prove to excite and delight you!</p>
  </section>
</main>
</body>
</html>
```